Saffron Lantern Court Business Card

I am looking for a business card desgined for my restaurant. It is an Indian restaurant, we are looking for something thats modern, yet traditional with the indian culture, we are looking for colors that match our logo. The logo is a design of the building with the name of the restaurant. for more information on the restaurant go to www.saffronlanterncourt.example

Industry/Entity Type

Indian Restaurant

Contact Information for Business Card

we are looking for somthing thats modern, yet traditional with the indian culture, we are looking for colors that match our logo. The logo is a design of the building with the name of the restaurant. for more information on the restaurant go to www.saffronlanterncourt.example

Requirements
Must have
• The logo that is attached,
• Name: Harvinder Oberoi,
• address of the restaurant: 7328 West Larkspur Rd, Phoenix, Arizona, 85213
• Phone: (602) 555-0147
• Fax: (602) 555-0193
• Restaurant Catering Banquet
• Website: www.SaffronLanternCourt.example
Nice to have
• wanted to get something that goes with the theme of the restaurant, which is traditional but also keep a very professional and modern touch

```html
<!DOCTYPE html>
<html lang="en">
<head>
<meta charset="utf-8">
<title>Saffron Lantern Court – Business Card</title>
<link rel="stylesheet" href="https://fonts.googleapis.com/css2?family=Roboto:wght@300;400;500&display=swap">
<style>
  :root {
    --page: #eceae6;
    --paper: #ffffff;
    --crimson: #a8232c;
    --saffron: #ee6a1f;
    --ink: #555555;
    --cream: #fbf3ea;
    --sketch-front: #f6c9a8;
    --sketch-back: #c4545a;
  }
  * { box-sizing: border-box; margin: 0; padding: 0; }
  html, body {
    width: 1200px; height: 950px; overflow: hidden;
    background: var(--page);
    font-family: "Roboto", Arial, sans-serif;
  }
  .stage {
    width: 1200px; height: 950px;
    display: flex; flex-direction: column; align-items: center; justify-content: center;
    gap: 40px;
  }
  .card {
    position: relative;
    width: 700px; height: 410px;
    border-radius: 4px;
    overflow: hidden;
    box-shadow: 0 6px 20px rgba(0,0,0,0.12);
  }

  /* Shared brand block */
  .wordmark {
    font-family: "Roboto", Arial, sans-serif;
    font-weight: 500;
    text-transform: uppercase;
    text-align: center;
    line-height: 1.1;
    letter-spacing: 2px;
  }

  /* Front */
  .card--front { background: var(--paper); }
  .edge-band {
    position: absolute; top: 0; right: 0; width: 16px; height: 100%;
    display: flex; flex-direction: column;
  }
  .edge-saffron { flex: 0 0 48%; background: var(--saffron); }
  .edge-crimson { flex: 1; background: var(--crimson); }

  .brand-front {
    position: absolute; top: 28px; right: 58px; width: 230px;
    display: flex; flex-direction: column; align-items: center; gap: 10px;
  }
  .brand-front .building-sketch { width: 180px; height: 48px; display: block; }
  .brand-front .wordmark { color: var(--crimson); font-size: 24px; }

  .tagline {
    position: absolute; left: 46px; top: 190px;
    color: var(--saffron); font-size: 13px; letter-spacing: 2px;
    text-transform: uppercase;
  }
  .divider {
    position: absolute; left: 46px; right: 46px; top: 222px;
    height: 1px; background: var(--saffron); opacity: 0.7;
  }
  .address {
    position: absolute; right: 58px; top: 242px;
    text-align: right; color: var(--ink); font-style: normal;
    font-size: 16px; line-height: 1.55;
  }
  .person { position: absolute; left: 46px; top: 242px; }
  .person-name {
    color: var(--crimson); font-size: 21px; font-weight: 500;
    letter-spacing: 0.5px; text-transform: uppercase;
  }
  .person-title {
    color: var(--saffron); font-size: 14px; letter-spacing: 1px;
    text-transform: uppercase; margin-top: 2px;
  }
  .contact-list { list-style: none; margin-top: 12px; }
  .contact-list li {
    display: flex; align-items: center; gap: 10px;
    color: var(--ink); font-size: 14px; line-height: 1.7;
  }
  .contact-list .label { color: var(--crimson); font-weight: 500; width: 14px; text-align: center; font-size: 11px; }
  .contact-list svg { width: 14px; height: 14px; fill: var(--crimson); flex: none; }

  /* Back */
  .card--back { background: var(--crimson); }
  .brand-back {
    position: absolute; top: 50%; left: 50%; transform: translate(-50%, -50%);
    display: flex; flex-direction: column; align-items: center; gap: 14px;
  }
  .brand-back .building-sketch { width: 220px; height: 64px; display: block; }
  .brand-back .wordmark { color: var(--cream); font-size: 34px; }
  .site-vertical {
    position: absolute; left: 36px; top: 50%;
    transform: translate(-50%, -50%) rotate(-90deg);
    color: var(--cream); font-size: 14px; letter-spacing: 0.6px; white-space: nowrap;
  }
  .social-marks {
    position: absolute; right: 28px; top: 50%; transform: translateY(-50%);
    display: flex; flex-direction: column; gap: 10px;
  }
  .social-marks span {
    display: block; width: 16px; height: 16px; border-radius: 3px;
    background: var(--cream);
  }
</style>
</head>
<body>
<main class="stage">

  <section class="card card--front" aria-label="Business card front">
    <div class="brand-front">
      <svg class="building-sketch" role="img" aria-label="Line drawing of the restaurant building" viewBox="0 0 180 48" preserveAspectRatio="none">
        <rect width="180" height="48" rx="4" fill="var(--sketch-front)"/>
      </svg>
      <div class="wordmark">Saffron<br>Lantern<br>Court</div>
    </div>

    <div class="tagline">Restaurant · Catering · Banquet</div>
    <div class="divider"></div>

    <div class="person">
      <div class="person-name">Harvinder Oberoi</div>
      <div class="person-title">President</div>
      <ul class="contact-list">
        <li>
          <svg viewBox="0 0 24 24" aria-hidden="true"><path d="M6.6 10.8a15.1 15.1 0 0 0 6.6 6.6l2.2-2.2c.3-.3.7-.4 1-.2 1.1.4 2.3.6 3.6.6.6 0 1 .4 1 1V20c0 .6-.4 1-1 1A17 17 0 0 1 3 4c0-.6.4-1 1-1h3.5c.6 0 1 .4 1 1 0 1.3.2 2.5.6 3.6.1.3 0 .7-.2 1z"/></svg>
          (602) 555-0147
        </li>
        <li>
          <span class="label">F</span>
          (602) 555-0193
        </li>
        <li>
          <svg viewBox="0 0 24 24" aria-hidden="true"><circle cx="12" cy="12" r="10"/><circle cx="12" cy="12" r="4" fill="#ffffff"/></svg>
          www.saffronlanterncourt.example
        </li>
      </ul>
    </div>

    <address class="address">
      7328 West Larkspur Road<br>
      Phoenix, Arizona 85213
    </address>

    <div class="edge-band" aria-hidden="true">
      <div class="edge-saffron"></div>
      <div class="edge-crimson"></div>
    </div>
  </section>

  <section class="card card--back" aria-label="Business card back">
    <div class="brand-back">
      <svg class="building-sketch" role="img" aria-label="Line drawing of the restaurant building" viewBox="0 0 220 64" preserveAspectRatio="none">
        <rect width="220" height="64" rx="4" fill="var(--sketch-back)"/>
      </svg>
      <div class="wordmark">Saffron<br>Lantern<br>Court</div>
    </div>
    <div class="site-vertical">www.saffronlanterncourt.example</div>
    <div class="social-marks" aria-label="Social media links">
      <span></span><span></span><span></span><span></span>
    </div>
  </section>

</main>
</body>
</html>
```